Cosmetic injections clinic needs a fresh looking business card

We need a business card using the supplied logo and color scheme to attract future clients to our clinic. It should be modern and fresh, eye catching and not too busy. Simple and to the point is best. I would like two sided designs with the front indicating address and contact information, and the back in full color with white logo and descriptive information also provided.
Target Market(s)
Clients looking for non surgical beauty enhancements.
Contact Information for Business Card
MeloraSkin
14, 618 Birchmont Way
St. Albert, Alberta
K2P 7W3
Phone: 587-412-6630
Email: info@meloraskin.com
Requirements
Must have
- -Logo supplied with the name and address of the clinic
- -Back of card in full color with white logo with A small line of text indicating both of the following: Anti aging consultants and cosmetic injectables
- Located inside the Voyager Wellness Group

```html
<!DOCTYPE html>
<html lang="en">
<head>
<meta charset="utf-8">
<title>MeloraSkin Business Card</title>
<link href="https://fonts.googleapis.com/css2?family=Roboto:wght@400;500&family=Roboto+Condensed:wght@700&display=swap" rel="stylesheet">
<style>
  :root {
    --backdrop: #2b2b2b;
    --card-white: #f3f3f3;
    --purple: #6a3f98;
    --pink: #e2439a;
    --teal: #2fbfa4;
    --ink: #4a4a4a;
    --rule: #cfcfcf;
    --white: #ffffff;
  }
  * { margin: 0; padding: 0; box-sizing: border-box; }
  html, body {
    width: 1200px; height: 960px; overflow: hidden;
    background: var(--backdrop);
    font-family: "Roboto", Arial, sans-serif;
  }
  .canvas { position: relative; width: 1200px; height: 960px; }
  .card {
    position: absolute; width: 600px; height: 343px;
    border-radius: 20px; overflow: hidden;
  }
  .card-front { left: 302px; top: 124px; background: var(--card-white); }
  .card-back { left: 299px; top: 493px; background: var(--pink); }

  .brand {
    position: absolute; left: 66px; top: 118px;
    display: flex; align-items: center; gap: 12px;
  }
  .brand-dot { width: 34px; height: 34px; border-radius: 50%; background: var(--pink); }
  .brand-name { font-size: 36px; font-weight: 500; color: var(--purple); letter-spacing: 0.3px; }

  .divider {
    position: absolute; left: 326px; top: 71px;
    width: 1px; height: 172px; background: var(--rule);
  }
  .contact { position: absolute; left: 354px; top: 70px; color: var(--ink); }
  .person-name {
    font-family: "Roboto Condensed", "Arial Narrow", sans-serif;
    font-weight: 700; font-size: 23px; color: var(--purple); line-height: 26px;
  }
  .person-title { font-size: 15px; color: var(--pink); line-height: 18px; letter-spacing: 0.3px; }
  .address { margin-top: 12px; font-size: 15px; line-height: 18px; }
  .reach { margin-top: 10px; font-size: 15px; line-height: 19px; }
  .reach-line { display: flex; align-items: center; gap: 7px; }
  .reach-line svg { width: 13px; height: 13px; fill: var(--purple); flex: none; }

  .wave { position: absolute; left: 0; top: 0; width: 600px; height: 343px; }
  .website {
    position: absolute; right: 68px; top: 316px;
    font-size: 14px; line-height: 18px; letter-spacing: 1.6px; color: var(--white);
  }

  .back-brand {
    position: absolute; left: 0; right: 0; top: 140px;
    display: flex; justify-content: center; align-items: center; gap: 14px;
  }
  .back-brand .brand-dot { width: 40px; height: 40px; background: var(--white); }
  .back-brand .brand-name { color: var(--white); font-size: 44px; }
  .tagline {
    position: absolute; left: 0; right: 0; top: 268px;
    text-align: center; color: var(--white); font-size: 15px; line-height: 19px;
  }
  .tagline-rule { width: 310px; height: 1px; background: var(--white); margin: 4px auto 3px; opacity: 0.85; }
</style>
</head>
<body>
<main class="canvas">
  <section class="card card-front">
    <svg class="wave" viewBox="0 0 600 343" aria-hidden="true">
      <path d="M0 288 C80 312 170 318 250 314 C170 318 80 310 0 302 Z" fill="var(--teal)"/>
      <path d="M0 309 C150 337 300 300 600 298 L600 343 L0 343 Z" fill="var(--white)"/>
      <path d="M420 300 C500 290 560 290 600 292 L600 302 C550 300 480 302 420 300 Z" fill="var(--pink)"/>
      <path d="M0 316 C150 344 300 306 600 306 L600 343 L0 343 Z" fill="var(--purple)"/>
    </svg>

    <div class="brand">
      <span class="brand-dot"></span>
      <span class="brand-name">MeloraSkin</span>
    </div>

    <div class="divider"></div>

    <div class="contact">
      <div class="person-name">DANA WHITFIELD</div>
      <div class="person-title">CEO/FOUNDER</div>
      <div class="address">
        MeloraSkin<br>
        14, 618 Birchmont Way<br>
        St. Albert, Alberta<br>
        K2P 7W3
      </div>
      <div class="reach">
        <div class="reach-line">
          <svg viewBox="0 0 24 24" aria-hidden="true"><path d="M6.6 10.8a15.1 15.1 0 0 0 6.6 6.6l2.2-2.2a1 1 0 0 1 1-.25 11.4 11.4 0 0 0 3.6.57 1 1 0 0 1 1 1V20a1 1 0 0 1-1 1A17 17 0 0 1 3 4a1 1 0 0 1 1-1h3.5a1 1 0 0 1 1 1c0 1.25.2 2.45.57 3.57a1 1 0 0 1-.25 1z"/></svg>
          <span>587-412-6630</span>
        </div>
        <div class="reach-line">
          <svg viewBox="0 0 24 24" aria-hidden="true"><path d="M2 5h20v14H2z"/><path d="M3 6.5l9 6.5 9-6.5" fill="none" stroke="var(--card-white)" stroke-width="1.8"/></svg>
          <span>info@meloraskin.com</span>
        </div>
      </div>
    </div>

    <div class="website">www.meloraskin.com</div>
  </section>

  <section class="card card-back">
    <div class="back-brand">
      <span class="brand-dot"></span>
      <span class="brand-name">MeloraSkin</span>
    </div>
    <div class="tagline">
      <div>Anti aging consultants &amp; cosmetic injectables</div>
      <div class="tagline-rule"></div>
      <div>Located inside the Voyager Wellness Group</div>
    </div>
  </section>
</main>
</body>
</html>
```